Dale Porcher Announces his new career move! 8x5 card please.

Associate Broker DALE PORCHER is proud to announce his new affiliation with m.voller sandy cove homes, ltd.

His goal remains to meet all your real estate needs. Prepare to renew your seasonal rental for 2016...with the full support of his new office, Dale can handle your renewal seamlessly.

Prepared to purchase? With access to every property on the market...Dale can show you how easy it making your summer dreams come true can be.

Thinking about selling? m.voller sandy cove homes, ltd. now offers the benefits of the Shared Offering Registry (SOR) to all sellers. In cooperation with SOR Sellers receive the maximum worldwide exposure, Purchasers receive a larger volume of properties to view and in cooperation with other agents, the transaction is handled professionally!!!!

I will send logo and photo of Dale Porcher separately. Thank you. M-
Updates

Project Deadline Extended Reason: I would need the cards to be delivered to my office by Friday June 26th for delivery to the public on the 27th. Thank you. Added Wednesday, June 17, 2015

Target Market(s)

Tenants, Sellers & Buyers

Industry/Entity Type

Broker

Font styles to use
Sans Serif

Requirements
Must have
• I attached logo and photo of Dale. Added a better photo of Dale.
Nice to have
• A photo of a property we have listed. I added a couple to choose from.
Should not have
• No Red color

```html
<!DOCTYPE html>
<html lang="en">
<head>
<meta charset="utf-8">
<title>Dale Porcher – Announcement Card</title>
<link rel="stylesheet" href="https://fonts.googleapis.com/css2?family=PT+Sans:wght@400;700&display=swap">
<style>
  :root {
    --paper: #ffffff;
    --green-light: #1f8e6b;
    --green-dark: #0e7455;
    --ink-white: #ffffff;
    --icon-dark: #1f2a26;
    --logo-ink: #1d1d1b;
    --rule: #dcdcdc;
    --stamp-border: #cfcfcf;
    --photo-light: #d9d9d6;
    --photo-mid: #8f908c;
    --photo-dark: #4a4b48;
  }
  * { margin: 0; padding: 0; box-sizing: border-box; }
  html, body {
    width: 1200px; height: 879px; overflow: hidden;
    background: var(--paper);
    font-family: "PT Sans", Arial, sans-serif;
  }
  .card { position: relative; width: 1200px; height: 879px; background: var(--paper); }

  .brand {
    position: absolute; right: 625px; top: 28px;
    display: flex; align-items: center; gap: 10px;
    color: var(--logo-ink); font-weight: 700; font-size: 22px; letter-spacing: -0.2px;
    white-space: nowrap;
  }
  .brand-mark { width: 14px; height: 14px; background: var(--green-dark); }

  .interior-photo {
    position: absolute; left: 0; top: 78px; width: 579px; height: 232px;
    background: linear-gradient(180deg, var(--photo-light) 0%, var(--photo-mid) 55%, var(--photo-dark) 100%);
  }
  .photo-notch { position: absolute; left: 0; top: 78px; }

  .info-band {
    position: absolute; left: 0; top: 274px; width: 579px; height: 451px;
    background: linear-gradient(180deg, rgba(31,142,107,0.55) 0px, var(--green-light) 40px, var(--green-dark) 100%);
  }
  .points { position: absolute; left: 0; top: 318px; width: 579px; }
  .point {
    position: absolute; left: 83px; color: var(--ink-white);
    font-size: 19.5px; line-height: 25.5px; white-space: nowrap;
  }
  .point strong { font-weight: 700; }
  .point-renew { top: 0; }
  .point-buy { top: 103px; }
  .point-sell { top: 203px; }
  .point-icon { position: absolute; left: 29px; width: 44px; height: 44px; }
  .icon-renew { top: 4px; }
  .icon-buy { top: 118px; }
  .icon-sell { top: 201px; }

  .stamp-box {
    position: absolute; left: 907px; top: 27px; width: 267px; height: 253px;
    border: 2px solid var(--stamp-border);
  }
  .address-line { position: absolute; left: 645px; width: 497px; height: 3px; background: var(--rule); }
  .line-1 { top: 395px; }
  .line-2 { top: 476px; }
  .line-3 { top: 554px; }
  .line-4 { top: 632px; }
</style>
</head>
<body>
<div class="card">
  <div class="brand"><span class="brand-mark"></span>m.voller sandy cove homes, ltd.</div>

  <div class="interior-photo" role="img" aria-label="Photo of a bright living room with fireplace, sofas and lamps"></div>
  <svg class="photo-notch" width="190" height="70" viewBox="0 0 190 70" aria-hidden="true">
    <polygon points="0,0 183,0 105,62 0,0" fill="var(--paper)"/>
  </svg>

  <div class="info-band"></div>

  <div class="points">
    <svg class="point-icon icon-renew" viewBox="0 0 44 44" aria-hidden="true">
      <circle cx="22" cy="22" r="21" fill="var(--icon-dark)" stroke="#fff" stroke-width="1.5"/>
      <path d="M13 22 L22 13 L31 13 L31 22 L22 31 Z" fill="none" stroke="#fff" stroke-width="2.2" stroke-linejoin="round"/>
      <circle cx="26.5" cy="17.5" r="2" fill="#fff"/>
    </svg>
    <p class="point point-renew"><strong>Prepare to renew your seasonal rental for 2016...</strong> with<br>the full support of his new office, Dale can handle your<br>renewal seamlessly.</p>

    <svg class="point-icon icon-buy" viewBox="0 0 44 44" aria-hidden="true">
      <circle cx="22" cy="22" r="21" fill="var(--icon-dark)" stroke="#fff" stroke-width="1.5"/>
      <circle cx="16" cy="17" r="5" fill="none" stroke="#fff" stroke-width="2.2"/>
      <path d="M19.5 20.5 L30 31 M26 27 L29 24 M28.5 29.5 L31 27" stroke="#fff" stroke-width="2.2" stroke-linecap="round"/>
    </svg>
    <p class="point point-buy"><strong>Prepared to purchase?</strong> With access to every property on<br>the market...Dale can show you how easy it making your<br>summer dreams come true can be.</p>

    <svg class="point-icon icon-sell" viewBox="0 0 44 44" aria-hidden="true">
      <circle cx="22" cy="22" r="21" fill="var(--icon-dark)" stroke="#fff" stroke-width="1.5"/>
      <path d="M11 22 L22 12 L33 22" fill="none" stroke="#fff" stroke-width="2.2" stroke-linejoin="round"/>
      <rect x="15" y="21" width="14" height="11" fill="none" stroke="#fff" stroke-width="2"/>
      <rect x="20" y="25" width="4" height="7" fill="#fff"/>
    </svg>
    <p class="point point-sell"><strong>Thinking about selling?</strong> m.voller sandy cove homes, ltd.<br>now offers the benefits of the Shared Offering Registry<br>(SOR) to all sellers. In cooperation with SOR Sellers receive<br>the maximum worldwide exposure, Purchasers receive a<br>larger volume of properties to view and in cooperation<br>with other agents, the transaction is handled<br>professionally!!!!</p>
  </div>

  <div class="stamp-box"></div>
  <div class="address-line line-1"></div>
  <div class="address-line line-2"></div>
  <div class="address-line line-3"></div>
  <div class="address-line line-4"></div>
</div>
</body>
</html>
```